WWW.VELTRONA.IT BUSINNES CARD

WE NEED A BUSINESS CARD . I HAVE A COMPANY IN ITALY NR 1 IN HAIR MEDICAL CARE AN HAIR REPLECEMENT . IN CARD I NEED WRITE WEB ADDRESS, MAIL , ADDRESS, TELEPHONE NUMBER , AND NAME
IN THE BACK SIDE I NEED MY DOCTOR LOGO .
MY WEB SITE IS WWW.VELTRONA.IT
Updates

Target Market(s)

CONSUMER B2C

Industry/Entity Type

Hair And Beauty

Contact Information for Business Card

I WANT A MEDICAL BUSINESS CARD.

Font styles to use
Other font styles liked:
• VERDANA

Colors
33a6d7
3176b5
85abd2
aedbee
eaf1f7
ffffff

Requirements
Must have
• I NEED MY LOGO AND LOGO OF DR VELTRONA

```html
<!DOCTYPE html>
<html lang="it">
<head>
<meta charset="utf-8">
<title>Veltrona – Business Card</title>
<link rel="stylesheet" href="https://fonts.googleapis.com/css2?family=Open+Sans:wght@400;600;700;800&display=swap">
<style>
  :root {
    --sky: #33a6d7;
    --royal: #3176b5;
    --soft-blue: #85abd2;
    --pale-blue: #aedbee;
    --mist: #eaf1f7;
    --white: #ffffff;
    --navy: #1f3f6e;
    --hair-dark: #4a2a12;
    --hair-mid: #8a5a2e;
    --ground: #c9926a;
    --page: #e6e9ee;
  }
  * { box-sizing: border-box; margin: 0; padding: 0; }
  html, body { width: 1200px; height: 900px; overflow: hidden; }
  body {
    background: var(--page);
    font-family: "Open Sans", Verdana, sans-serif;
    position: relative;
  }
  .card {
    position: absolute;
    top: 110px;
    width: 400px;
    height: 680px;
    border-radius: 34px;
    overflow: hidden;
    box-shadow: 0 10px 30px rgba(20, 40, 70, 0.18);
  }
  /* Front side */
  .card-front {
    left: 160px;
    background: linear-gradient(180deg, var(--sky) 0%, var(--pale-blue) 30%, var(--mist) 60%, var(--white) 100%);
  }
  .mascot {
    position: absolute;
    left: 70px;
    top: 70px;
    width: 230px;
    height: 560px;
    border-radius: 50% 50% 40% 40% / 20% 20% 12% 12%;
    background: linear-gradient(180deg, var(--hair-dark) 0%, var(--hair-mid) 55%, var(--ground) 100%);
    opacity: 0.85;
  }
  .doctor-name {
    position: absolute;
    left: 292px;
    top: 300px;
    writing-mode: vertical-rl;
    font-size: 40px;
    font-weight: 700;
    color: var(--royal);
    letter-spacing: 0.5px;
  }
  /* Back side */
  .card-back {
    left: 640px;
    background: linear-gradient(180deg, var(--white) 0%, var(--mist) 100%);
    padding: 48px 44px;
    color: var(--navy);
  }
  .brand {
    display: flex;
    align-items: center;
    gap: 12px;
  }
  .brand-dot {
    width: 40px;
    height: 40px;
    border-radius: 50%;
    background: var(--sky);
  }
  .brand-name {
    font-size: 44px;
    font-weight: 800;
    color: var(--royal);
    line-height: 1;
  }
  .tagline {
    margin-top: 8px;
    font-size: 13px;
    font-weight: 600;
    color: var(--sky);
    letter-spacing: 0.4px;
  }
  .swoosh { display: block; margin-left: -10px; }
  .swoosh-top { margin-top: 4px; }
  .person { margin-top: 118px; }
  .person-name {
    font-size: 26px;
    font-weight: 700;
    color: var(--sky);
  }
  .person-role {
    font-size: 17px;
    text-transform: uppercase;
    color: var(--navy);
  }
  .contacts { margin-top: 30px; list-style: none; }
  .contacts li {
    display: flex;
    align-items: center;
    gap: 12px;
    font-size: 19px;
    line-height: 30px;
    color: var(--navy);
  }
  .contacts svg { width: 18px; height: 18px; fill: var(--royal); flex: none; }
  .address {
    margin-top: 6px;
    font-size: 19px;
    line-height: 27px;
    font-style: normal;
    color: var(--navy);
  }
  .website {
    font-weight: 700;
    color: var(--royal);
  }
</style>
</head>
<body>
  <section class="card card-front" aria-label="Fronte del biglietto">
    <div class="mascot" role="img" aria-label="Illustrazione della mascotte: un capello in camice da medico che alza i pollici, su un ovale marrone"></div>
    <div class="doctor-name">dr. Veltrona</div>
  </section>

  <section class="card card-back" aria-label="Retro del biglietto">
    <div class="brand">
      <span class="brand-dot"></span>
      <span class="brand-name">Veltrona</span>
    </div>
    <p class="tagline">CURA E REINTEGRAZIONE DEI CAPELLI</p>
    <svg class="swoosh swoosh-top" width="320" height="40" viewBox="0 0 320 40">
      <path d="M4 34 Q150 40 316 4" fill="none" stroke="var(--sky)" stroke-width="3" stroke-linecap="round"/>
    </svg>

    <div class="person">
      <h1 class="person-name">Marco Bellandi</h1>
      <p class="person-role">Managing Director</p>
    </div>

    <ul class="contacts">
      <li>
        <svg viewBox="0 0 24 24"><path d="M6.6 10.8a15 15 0 0 0 6.6 6.6l2.2-2.2a1 1 0 0 1 1-.25 11.4 11.4 0 0 0 3.6.57 1 1 0 0 1 1 1V20a1 1 0 0 1-1 1A17 17 0 0 1 3 4a1 1 0 0 1 1-1h3.5a1 1 0 0 1 1 1c0 1.25.2 2.45.57 3.6a1 1 0 0 1-.25 1z"/></svg>
        333 412 7780
      </li>
      <li>
        <svg viewBox="0 0 24 24"><path d="M8 1h8a2 2 0 0 1 2 2v18a2 2 0 0 1-2 2H8a2 2 0 0 1-2-2V3a2 2 0 0 1 2-2zm0 3v14h8V4zm4 15.5a1 1 0 1 0 0 2 1 1 0 0 0 0-2z"/></svg>
        347 209 5561
      </li>
      <li>
        <svg viewBox="0 0 24 24"><path d="M2 5h20v14H2zm2 2v.5l8 5 8-5V7zm0 2.9V17h16V9.9l-8 5z"/></svg>
        m.bellandi@veltrona.it
      </li>
    </ul>

    <svg class="swoosh" width="320" height="40" viewBox="0 0 320 40">
      <path d="M4 36 Q150 40 316 6" fill="none" stroke="var(--sky)" stroke-width="3" stroke-linecap="round"/>
    </svg>

    <address class="address">
      18 Via Dante<br>
      Milano, MI 20121<br>
      <span class="website">www.veltrona.it</span>
    </address>
  </section>
</body>
</html>
```